Property Services Company Needs a Brochure Design

Looking for a new brochure design for an existing property services company.

We provide a range of property services from, market research, real estate brokerage, valuation and appraisal, property development and other real estate consulting services.

We would like a fresh modern brochure design with good graphics and features. Our colours are white, blue and orange.

The design should communicate, attention to detail, superior service delivery and distinction in results.
Updates

I would like the brochure to be roughly about 20 pages.

Containing the following,

1) An introduction
2) Contents Page
2) What we do
3) Our Services
4) Agency & Brokerage
5) Real Estate Consulting
6) Market Research
7) Appraisal & Valuation
8) Project Management
9) Property Development

I would also like icons to represent items 4,5,6,7,8 & 9, they should be represented vertically on each of the pages from the contents page and highlighted individually on the pages that they represent.. i.e. on appraisal & valuation page, all six icons will be arranged vertically and the appraisal and valuations icon will be highlighted.

I will also like to have images that depict the services on the various pages.

I have some pages I think will flow which I will upload shortly.

Industry/Entity Type

Real Estate

Font styles to use
Serif

Colors
f78f20
0455a3

```html
<!DOCTYPE html>
<html lang="en">
<head>
<meta charset="utf-8">
<title>Ashcombe Property Services – Brochure Cover</title>
<link rel="stylesheet" href="https://fonts.googleapis.com/css2?family=Nunito:wght@700;900&display=swap">
<style>
  :root {
    --brand-blue: #0455a3;
    --brand-blue-deep: #033e7a;
    --brand-orange: #f78f20;
    --brand-orange-light: #fba84a;
    --panel-light: #f1f1f2;
    --panel-shade: #d9dadc;
    --ink-dark: #3a3a3c;
    --curve-black: #111111;
    --white: #ffffff;
  }
  html, body {
    margin: 0;
    padding: 0;
    overflow: hidden;
    background: var(--white);
  }
  .cover {
    position: relative;
    width: 857px;
    height: 1200px;
    overflow: hidden;
    font-family: "Nunito", "Arial Rounded MT Bold", sans-serif;
  }
  .cover__art {
    display: block;
    width: 857px;
    height: 1200px;
  }
  .brand-name {
    font-family: "Nunito", sans-serif;
    font-weight: 700;
    fill: var(--ink-dark);
  }
  .headline {
    font-family: "Nunito", sans-serif;
    font-weight: 900;
    fill: var(--brand-blue);
    stroke: var(--white);
    stroke-width: 10px;
    stroke-linejoin: round;
    paint-order: stroke fill;
  }
  .headline--light {
    font-weight: 700;
    stroke-width: 8px;
  }
</style>
</head>
<body>
<main class="cover">
  <svg class="cover__art" viewBox="0 0 857 1200" xmlns="http://www.w3.org/2000/svg">
    <defs>
      <linearGradient id="sky-band" x1="0" y1="0" x2="0" y2="1">
        <stop offset="0" stop-color="var(--brand-blue)"/>
        <stop offset="1" stop-color="var(--brand-blue-deep)"/>
      </linearGradient>
      <linearGradient id="panel-fill" x1="0" y1="0" x2="1" y2="0">
        <stop offset="0" stop-color="var(--panel-shade)"/>
        <stop offset="0.15" stop-color="var(--panel-light)"/>
        <stop offset="0.85" stop-color="var(--panel-light)"/>
        <stop offset="1" stop-color="var(--panel-shade)"/>
      </linearGradient>
      <linearGradient id="photo-fill" x1="0" y1="0" x2="1" y2="1">
        <stop offset="0" stop-color="#5d6166"/>
        <stop offset="0.45" stop-color="#8b9096"/>
        <stop offset="0.75" stop-color="#a9c3e2"/>
        <stop offset="1" stop-color="#c9ccd0"/>
      </linearGradient>
      <linearGradient id="orange-fill" x1="0" y1="0" x2="0" y2="1">
        <stop offset="0" stop-color="var(--brand-orange)"/>
        <stop offset="1" stop-color="var(--brand-orange-light)"/>
      </linearGradient>
    </defs>

    <!-- top blue band -->
    <rect class="top-band" x="0" y="0" width="857" height="560" fill="url(#sky-band)"/>

    <!-- brand panel -->
    <rect class="brand-panel" x="161" y="0" width="343" height="474" fill="url(#panel-fill)"/>
    <g class="brand-lockup">
      <rect x="150" y="140" width="32" height="32" fill="var(--brand-orange)"/>
      <text class="brand-name" x="200" y="200" font-size="68">Ashcombe</text>
      <text class="brand-name" x="258" y="236" font-size="22">Property Services</text>
    </g>

    <!-- city photograph area -->
    <path class="photo-area" role="img" aria-label="Photograph looking up at tall city office towers against a blue sky"
          d="M0 490 Q 420 330 857 250 L857 900 Q 430 860 0 905 Z"
          fill="url(#photo-fill)"/>
    <path class="photo-edge" d="M0 490 Q 420 330 857 250" fill="none" stroke="var(--white)" stroke-width="10"/>

    <!-- dividing black curve and orange base -->
    <path class="base-curve" d="M0 890 Q 430 850 857 860 L857 900 Q 430 880 0 935 Z" fill="var(--curve-black)"/>
    <path class="base-band" d="M0 930 Q 430 878 857 895 L857 1200 L0 1200 Z" fill="url(#orange-fill)"/>

    <!-- headline -->
    <g class="headline-group">
      <text class="headline" x="666" y="895" font-size="62" text-anchor="end">Creative</text>
      <text class="headline" x="240" y="948" font-size="62">Solutions</text>
      <text class="headline headline--light" x="368" y="998" font-size="46">to all their</text>
      <text class="headline" x="120" y="1054" font-size="62">Real Estate</text>
      <text class="headline" x="472" y="1118" font-size="64">Needs</text>
    </g>
  </svg>
</main>
</body>
</html>
```